Professional/Sleek card design for athletic apparel brand

Athletic apparel brand. Mainly focused on lifting weights/gym workouts. Logo and brand are already created. Must use brand logo and name. Creativity is welcome. Looking for a clean, modern, and sexy design.

```html
<!DOCTYPE html>
<html lang="en">
<head>
<meta charset="utf-8">
<title>Iron and Grit – Business Card</title>
<link rel="stylesheet" href="https://fonts.googleapis.com/css2?family=Montserrat:wght@400;500;700;800&display=swap">
<style>
  :root {
    --bg: #d4d4d4;
    --card-dark: #2a2828;
    --card-dark-hi: #4a4848;
    --card-light: #f0f0f0;
    --ink: #1c1c1c;
    --ink-soft: #555555;
    --white: #ffffff;
    --tab-grey: #474747;
  }
  * { margin: 0; padding: 0; box-sizing: border-box; }
  html, body { width: 1200px; height: 1200px; overflow: hidden; }
  body {
    background: var(--bg);
    font-family: "Montserrat", sans-serif;
    position: relative;
  }
  .card {
    position: absolute;
    left: 220px;
    width: 760px;
    height: 434px;
    border-radius: 26px;
    overflow: hidden;
  }
  .card--front {
    top: 110px;
    background: linear-gradient(110deg, var(--card-dark-hi) 0%, var(--card-dark) 55%, #1f1d1d 100%);
  }
  .card--back {
    top: 640px;
    background: var(--card-light);
  }
  .brand {
    position: absolute;
    display: flex;
    align-items: center;
    gap: 16px;
    font-weight: 700;
    letter-spacing: 0.42em;
    text-transform: uppercase;
    white-space: nowrap;
  }
  .brand__dot {
    border-radius: 50%;
    flex: none;
  }
  .card--front .brand {
    left: 0; right: 0; top: 190px;
    justify-content: center;
    color: var(--white);
    font-size: 30px;
  }
  .card--front .brand__dot { width: 22px; height: 22px; background: var(--white); }
  .card--back .brand {
    left: 60px; top: 96px;
    color: var(--ink);
    font-size: 21px;
  }
  .card--back .brand__dot { width: 16px; height: 16px; background: var(--ink); }

  .edge-band {
    position: absolute;
    right: 0;
    width: 30px;
    background: var(--ink);
  }
  .edge-band--top { top: 0; height: 150px; border-bottom-left-radius: 14px; }
  .edge-band--bottom { bottom: 0; height: 224px; border-top-left-radius: 14px; }
  .edge-tab {
    position: absolute;
    right: 0; top: 166px;
    width: 30px; height: 28px;
    background: var(--tab-grey);
    border-radius: 10px 0 0 10px;
  }

  .person {
    position: absolute;
    right: 72px; top: 138px;
    text-align: right;
  }
  .person__name { font-size: 34px; font-weight: 800; color: var(--ink); line-height: 1.1; }
  .person__role { font-size: 18px; font-weight: 500; color: var(--ink-soft); margin-top: 4px; }

  .contact {
    position: absolute;
    left: 84px; top: 258px;
    color: var(--ink-soft);
    font-size: 19px;
    line-height: 1.3;
  }
  .contact__address { margin-bottom: 8px; }
  .contact__list { list-style: none; }
  .contact__item { display: flex; align-items: center; gap: 12px; }
  .contact__icon { width: 18px; height: 18px; flex: none; }
</style>
</head>
<body>

<section class="card card--front" aria-label="Card front">
  <div class="brand"><span class="brand__dot"></span>Iron and Grit</div>
</section>

<section class="card card--back" aria-label="Card back">
  <div class="edge-band edge-band--top"></div>
  <div class="edge-tab"></div>
  <div class="edge-band edge-band--bottom"></div>

  <div class="brand"><span class="brand__dot"></span>Iron and Grit</div>

  <div class="person">
    <p class="person__name">Marcus Vale</p>
    <p class="person__role">Founder &amp; Director</p>
  </div>

  <div class="contact">
    <p class="contact__address">4470 Harbor Lane<br>Fairview Ohio 45012</p>
    <ul class="contact__list">
      <li class="contact__item">
        <svg class="contact__icon" viewBox="0 0 24 24" aria-hidden="true"><path fill="#1c1c1c" d="M6.6 10.8a15 15 0 0 0 6.6 6.6l2.2-2.2c.3-.3.7-.4 1-.2 1.1.4 2.3.6 3.6.6.6 0 1 .4 1 1V20c0 .6-.4 1-1 1A17 17 0 0 1 3 4c0-.6.4-1 1-1h3.5c.6 0 1 .4 1 1 0 1.3.2 2.5.6 3.6.1.3 0 .7-.2 1z"/></svg>
        <span>(555)-014-2290</span>
      </li>
      <li class="contact__item">
        <svg class="contact__icon" viewBox="0 0 24 24" aria-hidden="true"><rect x="2" y="5" width="20" height="14" rx="1.5" fill="#1c1c1c"/><path d="M3 6l9 7 9-7" fill="none" stroke="#f0f0f0" stroke-width="1.6"/></svg>
        <span>info@ironandgrit.com</span>
      </li>
      <li class="contact__item">
        <svg class="contact__icon" viewBox="0 0 24 24" aria-hidden="true"><circle cx="12" cy="12" r="10" fill="#1c1c1c"/><path d="M2 12h20M12 2c3 3 3 17 0 20M12 2c-3 3-3 17 0 20" fill="none" stroke="#f0f0f0" stroke-width="1.3"/></svg>
        <span>www.ironandgrit.com</span>
      </li>
    </ul>
  </div>
</section>

</body>
</html>
```